Stationery Design Project - Professional Training Company

Full set of statinery in PDF and format that can be given to the printers

Letterhead
Business cards x 3
Compliments slip
Envelope
Updates

Many thanks for all your contributions, the quality of the designs is amazing.

Thank you all so much for your contribution to this project, I am very impressed with the designs and choice of designs, you are all clearly very talented individuals.

I hope to be making a decision on the final choice this evening UAE time.

Best regards and again thank you so much

Desmond

I would like to take this opportunity to thank you all for your contributions, I have been very impressed with each of the designs submitted.

I will shortly go back and give each of you a personal rating on each of your designs.

Again thank you all so much for your efforts

Best Regards

Desmond

Target Market(s)

We are a training company that provides IT training for Medical and Professional Staff, we train professional adults

Industry/Entity Type

Business

Requirements
Must have
• The letterhead and compliments slip must have at the bottom of the page:-

Bright Harbor Learning LLP operates as a limited liability partnership registered in England and Wales (with registered number OC742168)

Business Cards are to be made up for three people (details of those to be provided after appoval of design but are included in this project) and should contain:

Name
Title
Telephone
email
Address: P.O. Box 518243 Dubai UAE
web address: www.brightharborlearning.example
Nice to have
• Very clean and professional looking
Should not have
• No look to busy or ovr crowded

```html
<!DOCTYPE html>
<html lang="en">
<head>
<meta charset="utf-8">
<title>Bright Harbor Learning LLP – Business Cards</title>
<link rel="stylesheet" href="https://fonts.googleapis.com/css2?family=Didact+Gothic&family=Montserrat:wght@700&display=swap">
<style>
  :root {
    --backdrop: #e8e8eb;
    --card: #ffffff;
    --ink: #2a1f2c;
    --ink-soft: #4a4450;
    --plum: #6e0f5c;
    --plum-deep: #4f0a43;
    --leaf: #4f9a1d;
    --leaf-light: #6cb52a;
    --rule: #3a3340;
  }
  * { box-sizing: border-box; margin: 0; padding: 0; }
  html, body { width: 1200px; height: 934px; overflow: hidden; }
  body {
    background: var(--backdrop);
    font-family: "Didact Gothic", "Century Gothic", sans-serif;
    color: var(--ink);
    position: relative;
  }
  .card {
    position: absolute;
    top: 324px;
    width: 500px;
    height: 286px;
    background: var(--card);
    box-shadow: 0 6px 18px rgba(0,0,0,0.12);
    overflow: hidden;
  }
  .card--front { left: 70px; }
  .card--back { left: 630px; }

  .brand {
    position: absolute;
    display: flex;
    align-items: center;
    gap: 12px;
  }
  .brand__dot {
    width: 34px; height: 34px;
    border-radius: 50%;
    background: var(--plum);
    flex: none;
  }
  .brand__name {
    font-size: 21px;
    line-height: 1.05;
    color: var(--ink);
    max-width: 230px;
  }
  .card--front .brand { left: 30px; top: 38px; }

  .person {
    position: absolute;
    right: 30px;
    top: 100px;
    text-align: right;
  }
  .person__name {
    font-family: "Montserrat", sans-serif;
    font-weight: 700;
    font-size: 14px;
    letter-spacing: 0.5px;
    color: var(--ink);
  }
  .person__title { font-size: 12px; color: var(--ink-soft); margin-top: 2px; }

  .contact {
    position: absolute;
    left: 30px; right: 20px;
    bottom: 36px;
    display: flex;
    align-items: center;
    font-size: 11.5px;
    color: var(--ink-soft);
    letter-spacing: 0.3px;
  }
  .contact__group { display: flex; flex-direction: column; gap: 6px; }
  .contact__group--left { align-items: flex-end; }
  .contact__divider {
    width: 1px; height: 34px;
    background: var(--rule);
    margin: 0 16px;
  }
  .contact__line { display: flex; align-items: center; gap: 6px; white-space: nowrap; }
  .contact__icon { width: 11px; height: 11px; flex: none; }

  .card__band {
    position: absolute;
    left: 0; right: 0; bottom: 0;
    height: 14px;
    display: flex;
  }
  .card__band-leaf { flex: 0 0 57%; background: linear-gradient(90deg, var(--leaf-light), var(--leaf)); }
  .card__band-plum { flex: 1; background: var(--plum); }

  .card--back .brand { left: 36px; top: 104px; }
  .back__panel {
    position: absolute;
    right: 0; top: 0;
    width: 170px; height: 100%;
    background: linear-gradient(160deg, var(--plum-deep), var(--plum));
    clip-path: polygon(30% 0, 100% 0, 100% 100%, 70% 100%, 40% 60%, 28% 20%);
  }
  .back__web {
    position: absolute;
    left: 0; right: 0;
    bottom: 40px;
    text-align: center;
    font-size: 12.5px;
    color: var(--ink-soft);
    letter-spacing: 0.3px;
  }
</style>
</head>
<body>
  <section class="card card--front" aria-label="Business card front">
    <div class="brand">
      <span class="brand__dot"></span>
      <span class="brand__name">Bright Harbor Learning LLP</span>
    </div>
    <div class="person">
      <p class="person__name">DANIEL MARLOW</p>
      <p class="person__title">Managing Director</p>
    </div>
    <div class="contact">
      <div class="contact__group contact__group--left">
        <span class="contact__line">P.O. Box 518243, Dubai UAE</span>
        <span class="contact__line">
          <svg class="contact__icon" viewBox="0 0 12 12"><rect x="2" y="1" width="8" height="10" rx="1.5" fill="var(--plum)"/><rect x="4" y="2.5" width="4" height="5" fill="#fff"/></svg>
          Phone: +971 4 555 0142
        </span>
      </div>
      <span class="contact__divider"></span>
      <div class="contact__group">
        <span class="contact__line">
          <svg class="contact__icon" viewBox="0 0 12 12"><circle cx="6" cy="6" r="5" fill="var(--plum)"/><path d="M1 6h10M6 1c-2 3-2 7 0 10M6 1c2 3 2 7 0 10" stroke="#fff" stroke-width="0.8" fill="none"/></svg>
          www.brightharborlearning.example
        </span>
        <span class="contact__line">
          <svg class="contact__icon" viewBox="0 0 12 12"><rect x="0.5" y="2.5" width="11" height="7" fill="var(--plum)"/><path d="M0.5 2.5L6 7l5.5-4.5" stroke="#fff" stroke-width="0.9" fill="none"/></svg>
          info@brightharborlearning.example
        </span>
      </div>
    </div>
    <div class="card__band"><span class="card__band-leaf"></span><span class="card__band-plum"></span></div>
  </section>

  <section class="card card--back" aria-label="Business card back">
    <div class="back__panel"></div>
    <div class="brand">
      <span class="brand__dot"></span>
      <span class="brand__name">Bright Harbor Learning LLP</span>
    </div>
    <p class="back__web">www.brightharborlearning.example</p>
  </section>
</body>
</html>
```